THE REVEL OF GLIMBROOK Prospectus/Deck

We need a prospectus/deck made for this Halloween event called THE REVEL OF GLIMBROOK. Attached is the writeup, our logo, some background photos you can use, and photos of the actual town site. For the town photos (4) could you try to make them look greyscale or smokey? I attached a sample Prospectus/Deck that was created for another event of ours to give you an idea of layout and pages.

```html
<!DOCTYPE html>
<html lang="en">
<head>
<meta charset="utf-8">
<title>The Revel of Glimbrook – Prospectus</title>
<link rel="stylesheet" href="https://fonts.googleapis.com/css2?family=Poppins:wght@400;500;600;700&family=Oswald:wght@500;600&family=Creepster&display=swap">
<style>
:root{
  --page:#d3ced1;
  --ink:#0d0f10;
  --panel:#151819;
  --white:#f2f2f2;
  --muted:#c9cbc9;
  --gold:#e2b61f;
  --orange:#ef7d1a;
  --green:#8fbf3f;
  --green-dark:#4d7a2c;
  --card-gold:#b0721f;
  --card-green:#7fa34a;
}
*{margin:0;padding:0;box-sizing:border-box}
html,body{width:1200px;height:3651px;overflow:hidden;background:var(--page)}
body{position:relative;font-family:"Poppins",sans-serif;color:var(--white)}
.slide{position:absolute;left:140px;width:920px;height:648px;background:var(--ink);overflow:hidden;box-shadow:0 4px 10px rgba(0,0,0,.35)}
.slide > *{position:absolute}
.s1{top:118px}.s2{top:809px}.s3{top:1501px}.s4{top:2193px}.s5{top:2885px}
.photo{display:block}
.kicker{font-weight:600;letter-spacing:.35em;color:var(--gold);font-size:20px}
.wordmark{font-weight:700;color:var(--green);font-size:82px;letter-spacing:.02em;line-height:1}
.display{font-family:"Creepster",sans-serif;color:var(--green);line-height:1;letter-spacing:.02em}
.date{display:flex;align-items:center;gap:8px;font-family:"Oswald",sans-serif}
.date .month{font-family:"Poppins",sans-serif;font-weight:700;line-height:1;text-align:right}
.date .month b{display:block;color:var(--gold);font-size:21px}
.date .month i{display:block;font-style:normal;color:var(--orange);font-size:31px}
.date .day{font-size:48px;font-weight:600;color:var(--white);line-height:1}
.date sup{font-size:11px;vertical-align:top}
.date .to{width:20px;height:20px;border-radius:50%;background:var(--green);color:var(--ink);font-size:9px;display:flex;align-items:center;justify-content:center;font-family:"Poppins",sans-serif;font-weight:700}
.date .span{font-size:42px;color:var(--gold);font-weight:500}
.url{font-size:17px;letter-spacing:.08em;color:var(--white)}
.url span{color:var(--gold)}
.pageno{width:32px;height:32px;border-radius:50%;background:var(--green-dark);color:var(--white);font-size:13px;font-weight:600;display:flex;align-items:center;justify-content:center;right:80px;bottom:64px}
.body{font-size:10.5px;line-height:1.55;color:var(--muted)}
.body p+p{margin-top:14px}
.label{font-weight:500;font-size:20px;color:var(--white);text-transform:uppercase}
.price{font-weight:700;color:var(--gold);font-size:56px;line-height:1}
.price sup{font-size:26px;vertical-align:top}
.price small{font-size:30px;font-weight:400;color:var(--gold)}
.subhead{font-weight:700;color:var(--gold);font-size:22px}
.vendors{display:grid;grid-template-columns:200px 190px;gap:12px 0;font-size:10.5px;color:var(--muted)}
.vendors li{list-style:none;display:flex;gap:10px;align-items:center}
.vendors svg{flex:none}
.tier{width:208px;height:272px;border-radius:14px;background:var(--white);overflow:hidden;color:#222;border:3px solid var(--card-green)}
.tier header{background:var(--card-gold);color:var(--white);font-weight:600;font-size:11px;text-align:center;padding:8px 0}
.tier.silver header{background:var(--card-green)}
.tier .amount{background:#000;color:var(--white);font-weight:700;text-align:center;font-size:22px;line-height:1.1;margin:4px 5px;padding:6px 0}
.tier .amount sup{font-size:12px;vertical-align:top}
.tier ul{padding:6px 10px 0 12px;font-size:7.5px;line-height:1.4}
.tier li{list-style:none;position:relative;padding-left:10px;margin-bottom:3px}
.tier li::before{content:"";position:absolute;left:0;top:3px;width:5px;height:5px;border:1px solid #555;border-radius:50%}
</style>
</head>
<body>

<!-- Cover -->
<section class="slide s1">
  <svg class="photo" style="left:0;top:0" width="920" height="648" role="img" aria-label="Dark autumn forest with a hooded horned creature standing among fallen leaves">
    <defs>
      <radialGradient id="g1" cx="72%" cy="45%" r="60%"><stop offset="0" stop-color="#5a3a1c"/><stop offset=".12" stop-color="#3a2414"/><stop offset=".6" stop-color="#15110e"/><stop offset="1" stop-color="#0a0a0a"/></radialGradient>
    </defs>
    <rect width="920" height="648" fill="url(#g1)"/>
  </svg>
  <div class="kicker" style="left:114px;top:124px">THE REVEL OF</div>
  <div class="wordmark" style="left:55px;top:160px">GLIMBROOK</div>
  <div class="date" style="left:56px;top:318px">
    <div class="month"><b>OCTOBER</b><i>2023</i></div>
    <div class="day">6<sup>TH</sup></div><div class="to">TO</div><div class="day">31<sup>ST</sup></div>
    <div class="span">(17 DAYS)</div>
  </div>
  <div style="left:56px;top:394px;font-size:17px">1450 Lantern Road, Ashford Vale, Ontario K0A 2B0</div>
  <div class="url" style="left:60px;top:518px">www.<span>revelofglimbrook</span>.ca</div>
</section>

<!-- Introduction -->
<section class="slide s2">
  <svg class="photo" style="left:0;top:0" width="920" height="648" role="img" aria-label="Misty overgrown field with a pale robed figure wearing a branch headdress">
    <defs>
      <radialGradient id="g2" cx="76%" cy="38%" r="55%"><stop offset="0" stop-color="#4f6a44"/><stop offset=".45" stop-color="#23291f"/><stop offset="1" stop-color="#0d0f10"/></radialGradient>
    </defs>
    <rect width="920" height="648" fill="url(#g2)"/>
  </svg>
  <h1 class="display" style="left:78px;top:70px;font-size:84px">INTRODUCTION</h1>
  <div class="body" style="left:79px;top:180px;width:420px">
    <p>Welcome to The Revel of Glimbrook, where terror meets Hollywood magic! Step into our nightmare-inducing event set within a sprawling film studio lot at 1450 Lantern Road, Ashford Vale, Ontario K0A 2B0 which has been transformed into a chillingly realistic little town. As you enter, you will find yourself immersed in the eerie atmosphere of a bygone era, where each corner holds lurking horrors. Our haunted experience offers a unique opportunity for vendors to become part of the terror by occupying the shops that line the Main Street of this sinister town. From creepy curiosities to spine-chilling treats, your store front will become a focal point of fear, allowing visitors to not only scream but also shop amidst the horrors. Prepare for a spine-tingling journey like no other as you explore our haunted event in this hauntingly realistic town.</p>
    <p>The Revel of Glimbrook is an an exhilarating and spine-chilling haunted town experience that promises to deliver unforgettable thrills and scares. As we gear up for another terrifying season, we invite you to join us as a valued vendor or sponsor. This prospectus outlines the various opportunities available for your brand to be part of this highly anticipated event.</p>
  </div>
  <div class="url" style="left:79px;top:560px">www.<span>revelofglimbrook</span>.ca</div>
  <div class="pageno">01</div>
</section>

<!-- About -->
<section class="slide s3">
  <svg class="photo" style="left:0;top:0" width="920" height="648" role="img" aria-label="Grimy dark stone texture with faint cobweb">
    <rect width="920" height="648" fill="#15181a"/>
    <rect x="511" width="409" height="648" fill="#0c0d0e"/>
    <rect x="882" width="38" height="648" fill="#2a2c2d"/>
  </svg>
  <div style="left:96px;top:44px;font-size:36px;font-weight:700">ABOUT THE</div>
  <div class="kicker" style="left:110px;top:100px;font-size:13px">THE REVEL OF</div>
  <div class="wordmark" style="left:70px;top:118px;font-size:54px">GLIMBROOK</div>
  <div class="body" style="left:70px;top:218px;width:380px">The Revel of Glimbrook is a premier haunted town attraction known for its immersive and interactive experience that pushes the boundaries of fear. Our haunted town offers a meticulously designed setting with elaborate sets, talented actors, and cutting-edge special effects to create an atmosphere of horror and suspense. We attract a diverse audience of thrill-seekers, horror enthusiasts, families, and groups of friends, ensuring a wide reach for your brand.</div>
  <div style="left:74px;top:358px;font-size:17px;color:var(--gold);font-weight:500">EVENT DETAILS:</div>
  <div style="left:74px;top:388px;font-size:17px">DATE</div>
  <div class="date" style="left:74px;top:412px;transform:scale(.85);transform-origin:left top">
    <div class="month"><b>OCTOBER</b><i>2023</i></div>
    <div class="day">6<sup>TH</sup></div><div class="to">TO</div><div class="day">31<sup>ST</sup></div>
    <div class="span">(17 DAYS)</div>
  </div>
  <div style="left:74px;top:478px;font-size:17px">LOCATION</div>
  <div style="left:74px;top:502px;font-size:10px">1450 Lantern Road, Ashford Vale, Ontario K0A 2B0</div>
  <div class="url" style="left:78px;top:560px">www.<span>revelofglimbrook</span>.ca</div>
  <svg class="photo" style="left:511px;top:145px" width="181" height="134" role="img" aria-label="Greyscale street view of the town site"><defs><linearGradient id="p1" x1="0" y1="0" x2="0" y2="1"><stop offset="0" stop-color="#8a8c8d"/><stop offset="1" stop-color="#4a4c4d"/></linearGradient></defs><rect width="181" height="134" fill="url(#p1)"/></svg>
  <svg class="photo" style="left:702px;top:145px" width="180" height="134" role="img" aria-label="Greyscale smoky view of town buildings"><rect width="180" height="134" fill="#7d7f80"/></svg>
  <svg class="photo" style="left:511px;top:290px" width="371" height="188" role="img" aria-label="Greyscale aerial view of the film studio town lot"><defs><linearGradient id="p3" x1="0" y1="0" x2="0" y2="1"><stop offset="0" stop-color="#6f7172"/><stop offset="1" stop-color="#9a9c9d"/></linearGradient></defs><rect width="371" height="188" fill="url(#p3)"/></svg>
  <div class="pageno">02</div>
</section>

<!-- Vendor opportunities -->
<section class="slide s4">
  <svg class="photo" style="left:0;top:0" width="920" height="648" role="img" aria-label="Dark foggy background with tall grass and cobwebs">
    <defs><linearGradient id="g4" x1="0" y1="0" x2="0" y2="1"><stop offset="0" stop-color="#101213"/><stop offset=".6" stop-color="#1d221d"/><stop offset="1" stop-color="#141a12"/></linearGradient></defs>
    <rect width="920" height="648" fill="url(#g4)"/>
  </svg>
  <div style="left:44px;top:40px;font-size:26px;font-weight:700">VENDOR</div>
  <h2 class="display" style="left:40px;top:66px;font-size:64px;color:#a9b83a">OPPORTUNITIES</h2>
  <div class="label" style="left:40px;top:142px">ON-SITE VENDORS:</div>
  <div style="left:40px;top:180px;font-size:20px">Starting at</div>
  <div class="price" style="left:40px;top:205px"><sup>$</sup>2500 <small>+ HST</small></div>
  <div style="left:40px;top:264px;font-size:18px">(PER VENDOR; NO SHARING)</div>
  <div class="body" style="left:40px;top:292px;font-size:10px">depending on location and type of products/services sold and offered.</div>
  <div class="body" style="left:40px;top:318px;width:410px">Set up your booth within the haunted town premises and showcase your products or services to a captive audience in one of the existing buildings. Your brand will be exposed to thousands of visitors throughout the event. Examples of suitable vendors include:</div>
  <ul class="vendors" style="left:40px;top:390px">
    <li><svg width="20" height="20"><rect x="2" y="4" width="16" height="13" fill="none" stroke="#b58a2a" stroke-width="1.5"/></svg>Halloween costume shops</li>
    <li><svg width="20" height="20"><rect x="3" y="2" width="14" height="16" fill="none" stroke="#b58a2a" stroke-width="1.5"/></svg>Paranormal investigators or ghost tour guides</li>
    <li><svg width="20" height="20"><circle cx="10" cy="10" r="7" fill="none" stroke="#b58a2a" stroke-width="1.5"/></svg>Horror-themed merchandise</li>
    <li><svg width="20" height="20"><circle cx="10" cy="10" r="7" fill="none" stroke="#b58a2a" stroke-width="1.5"/></svg>Novelty and souvenir vendors</li>
    <li><svg width="20" height="20"><rect x="2" y="6" width="16" height="10" fill="none" stroke="#b58a2a" stroke-width="1.5"/></svg>Local/Artisan food vendors (pre-packaged items)</li>
    <li><svg width="20" height="20"><circle cx="10" cy="9" r="6" fill="none" stroke="#b58a2a" stroke-width="1.5"/></svg>Psychic</li>
    <li><svg width="20" height="20"><rect x="3" y="3" width="14" height="14" fill="none" stroke="#b58a2a" stroke-width="1.5"/></svg>Face painting and special effects makeup artists</li>
    <li><svg width="20" height="20"><path d="M10 2 17 10 10 18 3 10Z" fill="none" stroke="#b58a2a" stroke-width="1.5"/></svg>Metaphysical items and crystals</li>
  </ul>
  <div class="url" style="left:78px;top:564px">www.<span>revelofglimbrook</span>.ca</div>
  <div style="left:508px;top:180px;font-size:17px">FOOD TRUCKS</div>
  <div class="price" style="left:505px;top:198px"><sup>$</sup>2500 <small>+ HST max</small></div>
  <div style="left:505px;top:256px;font-size:17px">OF 3-4 TOTAL</div>
  <div class="subhead" style="left:502px;top:298px">PROMOTIONAL GIVEAWAYS</div>
  <div class="body" style="left:502px;top:328px;width:360px">Partner with us to provide branded merchandise or samples to be distributed to our visitors. This opportunity allows you to directly engage with attendees and create lasting impressions of your brand.</div>
  <div class="subhead" style="left:502px;top:410px">EXCLUSIVE SPONSORSHIP</div>
  <div class="body" style="left:502px;top:440px;width:360px">Become an exclusive sponsor of The Revel of Glimbrook. This comprehensive package offers maximum exposure and recognition for your brand. Benefits may include prominent logo placement, branding on event merchandise, on-site signage, social media promotions, and more. This option is ideal for businesses looking to establish a strong association with the haunted town and its audience.</div>
  <div class="pageno">03</div>
</section>

<!-- Sponsorship tiers -->
<section class="slide s5">
  <svg class="photo" style="left:0;top:0" width="920" height="648" role="img" aria-label="Dim grungy workshop interior with a menacing figure leaning on a bench">
    <defs><radialGradient id="g5" cx="70%" cy="40%" r="55%"><stop offset="0" stop-color="#4a3a30"/><stop offset=".55" stop-color="#211c19"/><stop offset="1" stop-color="#0e0e0e"/></radialGradient></defs>
    <rect width="920" height="648" fill="url(#g5)"/>
  </svg>
  <div style="left:44px;top:42px;font-size:26px;font-weight:700">SPONSORSHIP</div>
  <h2 class="display" style="left:40px;top:66px;font-size:64px;color:#a9b83a">TIERS</h2>
  <div class="body" style="left:40px;top:144px;width:460px;font-size:8px;line-height:1.5">We offer different sponsorship tiers to suit your marketing goals and budget. Please note that availability is limited for each tier, and commitments will be honored on a first-come, first-served basis. The sponsorship tiers include:</div>
  <article class="tier" style="left:40px;top:200px">
    <header>PLATINUM SPONSORSHIP</header>
    <div class="amount"><sup>$</sup>15,000<br>+ HST</div>
    <ul>
      <li>Prominent logo placement on all marketing materials, including website, posters, flyers, and social media promotions</li>
      <li>Exclusive branding on event merchandise</li>
      <li>On-site signage and banners featuring your brand</li>
      <li>Dedicated social media posts highlighting your sponsorship</li>
      <li>Recognition during event announcements and media interviews</li>
      <li>Complimentary tickets for your staff or clients</li>
    </ul>
  </article>
  <article class="tier" style="left:260px;top:200px">
    <header>PLATINUM SPONSORSHIP</header>
    <div class="amount"><sup>$</sup>10,000<br>+ HST</div>
    <ul>
      <li>Logo placement on select marketing materials, including website, posters, and social media promotions</li>
      <li>On-site signage featuring your brand</li>
      <li>Social media mentions acknowledging your sponsorship</li>
      <li>Complimentary tickets for your staff or clients</li>
    </ul>
  </article>
  <article class="tier silver" style="left:480px;top:200px">
    <header>SILVER SPONSORSHIP</header>
    <div class="amount"><sup>$</sup>5,000<br>+ HST</div>
    <ul>
      <li>Logo placement on event website and select marketing materials</li>
      <li>On-site signage featuring your brand</li>
      <li>Complimentary tickets for your staff or clients</li>
    </ul>
  </article>
  <div class="body" style="left:40px;top:490px;width:640px;font-size:8px;line-height:1.6">
    <p>We are open to customizing sponsorship packages to meet your specific needs and objectives.</p>
    <p style="margin-top:3px">If you are interested in becoming a vendor or sponsor for The Revel of Glimbrook, please contact us at the following: hello@lanternevents.ca</p>
    <p style="margin-top:3px">We would be delighted to discuss the available opportunities in more detail and tailor a package that aligns with your brand's goals.</p>
    <p style="margin-top:3px">Do not miss the chance to be part of a frightfully fantastic experience that will haunt your customers' memories for years to come. Join The Revel of Glimbrook as a vendor or sponsor and make this haunted town season one to remember!</p>
  </div>
  <div class="url" style="left:40px;top:590px">www.<span>revelofglimbrook</span>.ca</div>
  <div class="pageno">05</div>
</section>

</body>
</html>
```